Green Logistics / Last Mile Delivery Firm needs cool one-page website

FYI - We do have a detailed brief in the uploaded files section below
COMPANY
We recently launched the company Quillby Logistics which is a pioneer in urban green logistics and provides zero-emissions last mile delivery services (i.e. delivery of parcels with delivery vans to the doorstep of households) for its logistics and retail clients.
We take on urban parcel delivery for our clients with a 100% electric commercial vehicles fleet, fair and sustainable working conditions for our employees and an unparalleled professional and customer-focused mindset.
WEBSITE
In the detailed brief, we have provided examples to emulate. We need the design + coding of the website. Website needs to be friendly/optimized for and should open swiftly on both Android & iOS.
In general, the website should convey
- green mission of the company
- sustainability (good working conditions, focus on employees)
- customer orientation
- professionalism
DESIGN
In the detailed brief, we have provided designs to emulate.
Color design: we do have a logo which features 2 green colors (one lighter and one darker color tone). However, the colors on the website do not necessarily need to follow these 2 colors exactly as we are able to switch the logo colors.
Imagery: should reflect maybe 50% green/leaf/tree , 25% customer and employee orientation, and 25% logistics (here it's important that it is the last mile delivery, i.e. delivery with delivery vans to the doorstep of households)

```html
<!DOCTYPE html>
<html lang="en">
<head>
<meta charset="utf-8">
<title>Quillby Logistics – Sustainable Last Mile</title>
<link rel="stylesheet" href="https://fonts.googleapis.com/css2?family=Oswald:wght@400;500;600&family=Arimo:wght@400;700&display=swap">
<style>
:root{
  --green-dark:#1f9a3c;
  --green-mid:#2aa43c;
  --green-light:#74c02c;
  --ink:#2b2b2b;
  --text:#555;
  --muted:#888;
  --line:#dcdcdc;
  --soft-bg:#f4f4f4;
  --footer:#1f1f1f;
  --white:#fff;
}
*{box-sizing:border-box;margin:0;padding:0}
html,body{width:1200px;height:5333px;overflow:hidden}
body{font-family:"Arimo",Arial,sans-serif;color:var(--text);background:var(--white);position:relative}
.head{font-family:"Oswald",sans-serif;text-transform:uppercase;color:var(--ink);font-weight:500}
section,header,footer{position:absolute;left:0;width:1200px}
.abs{position:absolute}
.section-title{position:absolute;left:0;width:1200px;text-align:center;font-size:46px;line-height:1}
.title-bar{position:absolute;left:576px;width:48px;height:4px;background:var(--green-light)}

/* header */
.site-header{top:0;height:120px;background:var(--white)}
.brand{display:flex;align-items:center;gap:14px}
.brand-dot{width:54px;height:54px;border-radius:50%;background:var(--green-dark)}
.brand-name{font-family:"Oswald",sans-serif;font-weight:500;color:var(--green-dark);text-transform:uppercase;line-height:1;white-space:nowrap}
.top-contact{display:flex;align-items:center;gap:10px;font-family:"Oswald",sans-serif;font-size:15px;color:var(--green-dark);white-space:nowrap}
.top-contact .ic{width:54px;height:54px;border-radius:50%;background:var(--green-dark);display:flex;align-items:center;justify-content:center}
.top-contact.light{color:var(--green-light)}
.top-contact.light .ic{background:var(--green-light)}
.main-nav{display:flex;gap:50px;font-family:"Oswald",sans-serif;font-size:14px;color:var(--ink);white-space:nowrap}
.main-nav .active{color:var(--green-dark)}

/* hero */
.hero{top:120px;height:702px;background:linear-gradient(180deg,#c9cfd3 0%,#aab6bd 35%,#8e9a82 62%,#7b8a45 80%,#5f6e34 100%)}
.hero-title{position:absolute;left:0;width:1200px;text-align:center;color:var(--white);font-family:"Oswald",sans-serif;font-weight:500;text-transform:uppercase;text-shadow:0 2px 6px rgba(0,0,0,.35)}
.btn{display:flex;align-items:center;justify-content:center;border-radius:40px;font-family:"Oswald",sans-serif;text-transform:uppercase;color:var(--white)}
.btn-green{background:var(--green-mid);border:3px solid var(--white)}
.btn-ghost{border:2px solid var(--white)}

/* about */
.about{top:822px;height:745px}
.about-card{position:absolute;top:1037px;width:314px;height:453px;color:var(--white);text-align:center;padding:0 26px}
.about-card h3{font-family:"Oswald",sans-serif;font-weight:500;font-size:23px;margin-top:112px;margin-bottom:18px;text-transform:uppercase}
.about-card p{font-size:12.5px;line-height:26px}
.about-card p+p{margin-top:26px}
.card-icon{position:absolute;top:979px;width:140px;height:140px;border-radius:50%;border:5px solid var(--white);display:flex;align-items:center;justify-content:center}

/* compare */
.compare{top:1567px;height:797px;background:var(--soft-bg)}
.compare-box{position:absolute;left:124px;top:163px;width:950px;height:553px;background:var(--white);border:3px solid #d7d7d7;display:flex}
.compare-col{width:50%;position:relative}
.compare-col+.compare-col{border-left:2px solid #e2e2e2}
.compare-col h4{height:62px;line-height:62px;padding-left:26px;color:var(--white);font-family:"Oswald",sans-serif;font-weight:500;font-size:21px;text-transform:uppercase}
.compare-list{list-style:none;padding:44px 0 0 30px;width:420px}
.compare-list li{font-size:15.5px;color:#777;line-height:20px;margin-bottom:16px;padding-left:30px;position:relative}
.compare-list li::before{content:"";position:absolute;left:2px;top:5px;width:7px;height:7px;border-right:2px solid #555;border-top:2px solid #555;transform:rotate(45deg)}
.compare-list.struck li{text-decoration:line-through}
.illustration{position:absolute;border-radius:8px}

/* services */
.services{top:2364px;height:766px}
.services-intro{position:absolute;left:215px;width:770px;top:146px;text-align:center;font-size:14.5px;line-height:31px;color:#666}
.service-card{position:absolute;width:474px;height:195px;border:3px solid #e8e8e8;background:var(--white)}
.service-icon{position:absolute;left:14px;top:32px;width:124px;height:124px;border-radius:50%;display:flex;align-items:center;justify-content:center}
.service-card h4{position:absolute;left:172px;top:38px;font-family:"Oswald",sans-serif;font-weight:500;font-size:19px;color:var(--ink);text-transform:uppercase;white-space:nowrap}
.service-card .bar{position:absolute;left:172px;top:78px;width:40px;height:3px;background:var(--green-light)}
.service-card p{position:absolute;left:172px;top:100px;width:280px;font-size:14px;line-height:26px;color:#777}

/* cta */
.cta{top:3130px;height:486px;background:linear-gradient(100deg,#1f9440 0%,#3fa63b 45%,#86c83a 100%)}
.cta p{position:absolute;left:220px;width:760px;top:188px;text-align:center;color:var(--white);font-size:19px;line-height:38px}

/* careers */
.careers{top:3616px;height:855px}
.careers-text{position:absolute;left:230px;width:740px;top:143px;text-align:center;font-size:12.5px;line-height:29px;color:#666}
.careers-text p{margin-bottom:29px}
.accordion{position:absolute;left:193px;width:815px;top:596px}
.acc-row{height:71px;border-bottom:2px solid #e3e3e3;display:flex;align-items:center;gap:18px}
.acc-plus{width:46px;height:46px;border-radius:50%;border:2px solid #d5d5d5;display:flex;align-items:center;justify-content:center;color:var(--green-light);font-size:26px;font-weight:300}
.acc-row span{font-family:"Oswald",sans-serif;font-size:16px;color:var(--ink);text-transform:uppercase}

/* contact */
.contact{top:4471px;height:493px;background:var(--soft-bg)}
.info-item{position:absolute;left:112px;display:flex;gap:30px}
.info-item h5{font-family:"Oswald",sans-serif;font-weight:500;font-size:19px;color:var(--ink);text-transform:uppercase;margin-bottom:8px}
.info-item p{font-size:13px;color:#555}
.field{position:absolute;border-bottom:2px solid #d4d4d4;height:38px;font-size:13px;color:#444}

/* footer */
.site-footer{top:4964px;height:369px;background:var(--footer)}
.footer-nav{position:absolute;top:170px;left:0;width:1200px;display:flex;justify-content:center;font-family:"Oswald",sans-serif;font-size:16px;color:var(--white);text-transform:uppercase}
.footer-nav span{padding:0 40px;border-left:2px solid #aaa;line-height:18px}
.footer-nav span:first-child{border-left:0}
.social{position:absolute;top:220px;left:0;width:1200px;display:flex;justify-content:center;gap:6px}
.social i{width:36px;height:36px;border-radius:50%;border:2px solid var(--white)}
.copyright{position:absolute;top:295px;left:0;width:1200px;text-align:center;font-family:"Oswald",sans-serif;font-size:12px;color:var(--white);text-transform:uppercase}
.copyright em{font-style:normal;color:var(--green-light)}
</style>
</head>
<body>

<header class="site-header">
  <div class="brand abs" style="left:114px;top:28px">
    <div class="brand-dot"></div>
    <div class="brand-name" style="font-size:30px">Quillby Logistics</div>
  </div>
  <div class="top-contact abs" style="left:632px;top:16px">
    <div class="ic"><svg width="22" height="22" viewBox="0 0 24 24" fill="#fff"><path d="M6.6 10.8a15 15 0 0 0 6.6 6.6l2.2-2.2c.3-.3.7-.4 1-.2 1.1.4 2.3.6 3.6.6.6 0 1 .4 1 1V20c0 .6-.4 1-1 1A17 17 0 0 1 3 4c0-.6.4-1 1-1h3.5c.6 0 1 .4 1 1 0 1.3.2 2.5.6 3.6.1.3 0 .7-.2 1z"/></svg></div>
    <span>CALL US : 000-484-2790</span>
  </div>
  <div class="top-contact light abs" style="left:860px;top:16px">
    <div class="ic"><svg width="22" height="22" viewBox="0 0 24 24" fill="#fff"><path d="M6.6 10.8a15 15 0 0 0 6.6 6.6l2.2-2.2c.3-.3.7-.4 1-.2 1.1.4 2.3.6 3.6.6.6 0 1 .4 1 1V20c0 .6-.4 1-1 1A17 17 0 0 1 3 4c0-.6.4-1 1-1h3.5c.6 0 1 .4 1 1 0 1.3.2 2.5.6 3.6.1.3 0 .7-.2 1z"/></svg></div>
    <span>INFO@QUILLBYLOGISTICS.COM</span>
  </div>
  <nav class="main-nav abs" style="left:611px;top:86px">
    <span class="active">HOME</span><span>ABOUT</span><span>SERVICES</span><span>CAREERS</span><span>CONTACT</span>
    <span style="margin-left:-38px;color:var(--green-dark)">| &nbsp;EN &nbsp;▾</span>
  </nav>
</header>

<section class="hero">
  <div class="abs" role="img" aria-label="Photo of a white delivery truck driving on a motorway past green fields" style="inset:0"></div>
  <div class="brand abs" style="left:420px;top:130px">
    <div class="brand-dot" style="width:80px;height:80px"></div>
    <div class="brand-name" style="font-size:38px">Quillby Logistics</div>
  </div>
  <div class="hero-title" style="top:448px;font-size:38px">Quillby Logistics – Sustainable Last Mile</div>
  <div class="hero-title" style="top:505px;font-size:34px">Because we care about trees!</div>
  <div class="btn btn-green abs" style="left:500px;top:574px;width:200px;height:52px;font-size:20px">Get Started</div>
</section>

<section class="about">
  <div class="section-title head" style="top:60px">About Us</div>
  <div class="title-bar" style="top:118px"></div>
</section>
<div class="about-card" style="left:112px;background:var(--green-dark)">
  <h3>Wo We Are</h3>
  <p>Quillby Logistics is a pioneer in urban green logistics and provides zero-emissions last mile delivery services for its logistics and retail clients.</p>
  <p>We take on urban parcel delivery for our clients with a 100% electric commercial vehicles fleet, fair and sustainable working conditions for our employees and an unparalleled professional and customer focused mindset.</p>
</div>
<div class="about-card" style="left:443px;background:#5cb92d">
  <h3>Our Mission</h3>
  <p>To satisfy consumers' ever-rising desire to buy products online, the CO2 emissions from delivery traffic will increase by 32% in the top 100 cities globally until 2030.</p>
  <p>Our clients care about our planet the same way we do, which is why Quillby Logistics helps to make the planet a better place by running the most environ-mentally friendly urban last mile possible.</p>
</div>
<div class="about-card" style="left:774px;background:var(--green-dark)">
  <h3>Our Values</h3>
  <p>We see ourselves as a professional services company who strongly cares about the environment, its clients and their customers, as well as its employees.</p>
  <p>We believe that delivering parcels with zero emissions and providing a unique customer experience through a highly professional attitude and a great team the cornerstones for Quillby Logistics to operate in a sustainable yet profitable way.</p>
</div>
<div class="card-icon" style="left:199px;background:var(--green-dark)">
  <svg width="64" height="64" viewBox="0 0 64 64" fill="none" stroke="#fff" stroke-width="2.5"><circle cx="32" cy="18" r="10"/><path d="M12 58V44c0-8 8-14 20-14s20 6 20 14v14z"/><path d="M28 42a4 4 0 1 1 5 4v3M32 53v1"/></svg>
</div>
<div class="card-icon" style="left:530px;background:#5cb92d">
  <svg width="70" height="70" viewBox="0 0 64 64" fill="none" stroke="#fff" stroke-width="3"><circle cx="32" cy="34" r="24"/><circle cx="32" cy="34" r="15"/><circle cx="32" cy="34" r="6"/><path d="M32 34L52 14M46 12h8v8"/></svg>
</div>
<div class="card-icon" style="left:861px;background:var(--green-dark)">
  <svg width="68" height="68" viewBox="0 0 64 64" fill="none" stroke="#fff" stroke-width="2.5"><rect x="6" y="10" width="8" height="6"/><rect x="6" y="24" width="8" height="6"/><rect x="6" y="38" width="8" height="6"/><rect x="6" y="52" width="8" height="6"/><rect x="22" y="10" width="34" height="6"/><rect x="22" y="24" width="34" height="6"/><rect x="22" y="38" width="34" height="6"/><rect x="22" y="52" width="34" height="6"/></svg>
</div>

<section class="compare">
  <div class="section-title head" style="top:50px">Quillby Logistics Is...</div>
  <div class="title-bar" style="top:108px"></div>
  <div class="compare-box">
    <div class="compare-col">
      <h4 style="background:var(--green-light)">An Ordinary Parcel Delivery Firm</h4>
      <ul class="compare-list struck">
        <li>Polluting our cities</li>
        <li>Always in a rush</li>
        <li>Short-term oriented</li>
        <li>Focusing on profit only</li>
        <li>Yet another parcel delivery firm</li>
      </ul>
      <div class="illustration" role="img" aria-label="Illustration of a courier handing a parcel to a customer at her door" style="left:166px;top:330px;width:290px;height:205px;background:radial-gradient(ellipse at center,#dfe9f2 0%,#eef3f7 60%,#fff 100%)"></div>
    </div>
    <div class="compare-col">
      <h4 style="background:var(--green-dark)">A Pioneering Green Last Mile</h4>
      <ul class="compare-list">
        <li>Delivering parcels emissions-free</li>
        <li>Putting customer experience first</li>
        <li>Operating the business sustainably</li>
        <li>Focusing on the environment, customers &amp; employees</li>
        <li>A professional services company</li>
      </ul>
      <div class="illustration" role="img" aria-label="Illustration of delivery vans, parcels and a world map with location pins" style="left:80px;top:310px;width:380px;height:215px;background:radial-gradient(ellipse at center,#e4ecf6 0%,#f1f5fa 60%,#fff 100%)"></div>
    </div>
  </div>
</section>

<section class="services">
  <div class="section-title head" style="top:60px">Our Services</div>
  <div class="title-bar" style="top:118px"></div>
  <div class="services-intro">Quillby Logistics provides last mile delivery services in urban areas to clients in the logistics and retail space. Our permanent employees are all highly trained and commit to highest professional standards which we continuously review and further develop with them.</div>

  <div class="service-card" style="left:112px;top:269px">
    <div class="service-icon" style="background:var(--green-dark)"><svg width="70" height="50" viewBox="0 0 70 50" fill="none" stroke="#fff" stroke-width="3"><rect x="4" y="6" width="38" height="30"/><path d="M42 16h14l10 12v8H42z"/><circle cx="16" cy="40" r="5" fill="var(--green-dark)"/><circle cx="54" cy="40" r="5" fill="var(--green-dark)"/></svg></div>
    <h4>Zero-Emission Delivery</h4><div class="bar"></div>
    <p>We operate a 100% electric commercial vehicle fleet</p>
  </div>
  <div class="service-card" style="left:614px;top:269px">
    <div class="service-icon" style="background:var(--green-light)"><svg width="60" height="60" viewBox="0 0 60 60" fill="none" stroke="#fff" stroke-width="3"><circle cx="32" cy="16" r="9"/><path d="M16 56V40c0-7 7-12 16-12s16 5 16 12v16"/><rect x="6" y="34" width="14" height="12"/></svg></div>
    <h4>Highly Trained Delivery Drivers</h4><div class="bar"></div>
    <p>We only employ permanently, train far above average, and live a great team spirit</p>
  </div>
  <div class="service-card" style="left:112px;top:497px">
    <div class="service-icon" style="background:var(--green-light)"><svg width="60" height="52" viewBox="0 0 60 52" fill="none" stroke="#fff" stroke-width="3"><rect x="4" y="12" width="52" height="36" rx="3"/><path d="M22 12V5h16v7M4 28h52M26 24h8v8h-8z"/></svg></div>
    <h4>Professional All Around</h4><div class="bar"></div>
    <p>We honor our commitments and hold ourselves to the highest professional standards</p>
  </div>
  <div class="service-card" style="left:614px;top:497px">
    <div class="service-icon" style="background:var(--green-dark)"><svg width="64" height="64" viewBox="0 0 64 64" fill="none" stroke="#fff" stroke-width="3"><circle cx="32" cy="32" r="26"/><circle cx="32" cy="24" r="6"/><circle cx="20" cy="34" r="4"/><circle cx="44" cy="34" r="4"/><path d="M22 46c0-6 4-10 10-10s10 4 10 10M12 44c0-4 3-6 8-6M52 44c0-4-3-6-8-6"/></svg></div>
    <h4>Unparalleled Customer Focus</h4><div class="bar"></div>
    <p>We live a customer-oriented mindset, always measuring ourselves against their experience</p>
  </div>
</section>

<section class="cta" role="img" aria-label="Green-tinted photo of a truck at a logistics yard">
  <div class="section-title head" style="top:118px;color:var(--white);font-size:44px">Get in Touch with Quillby Logistics</div>
  <p>If you got excited, or have a question about our services, our approach, our jobs or just want to get in touch to chat about how green logistics can make the planet a little bit better, please get in touch!</p>
  <div class="btn btn-ghost abs" style="left:497px;top:323px;width:207px;height:54px;font-size:18px">Contact Us</div>
</section>

<section class="careers">
  <div class="section-title head" style="top:55px">Careers</div>
  <div class="title-bar" style="top:113px"></div>
  <div class="careers-text">
    <p>If you join Quillby Logistics, you join a family. We elevate one another, care for each other's wellbeing and growth, &amp; cele brate our successes. We strongly believe growth is a team sport and that every member of the family fully contri butes to the achievements of the company overall.</p>
    <p>At the heart of everything we do at Quillby Logistics is a relentless focus on our mission. That's why we aim to ensure our employees can follow their own passion at the workplace, be this working in a truly collaborative and caring team, putting a smile on a customer's face or making the world a better place.</p>
    <p>While we are helping our clients grow by delivering their parcels, we are also helping all our employees grow persona lly and professionally. We care about our employees' happiness and wellbeing which is why we provide additional benefits like supplementary health insurance.</p>
    <p>If you are excited about joining our Quillby Logistics family, please check out our open positions.</p>
  </div>
  <div class="accordion">
    <div class="acc-row"><div class="acc-plus">+</div><span>Your tasks as a delivery driver</span></div>
    <div class="acc-row"><div class="acc-plus">+</div><span>Required knowledge and skills</span></div>
    <div class="acc-row"><div class="acc-plus">+</div><span>What you can expected from the Quillby Logistics family</span></div>
  </div>
</section>

<section class="contact">
  <div class="section-title head" style="top:45px">Contact Us</div>
  <div class="info-item" style="top:148px">
    <svg width="36" height="44" viewBox="0 0 36 44" fill="none" stroke="var(--green-light)" stroke-width="2"><path d="M18 42S3 26 3 16a15 15 0 0 1 30 0c0 10-15 26-15 26z"/><circle cx="18" cy="16" r="5"/></svg>
    <div><h5>Address</h5><p>#145 Lorem Ipsum Dummy Text Lorem</p></div>
  </div>
  <div class="info-item" style="top:248px">
    <svg width="38" height="38" viewBox="0 0 24 24" fill="none" stroke="var(--green-light)" stroke-width="1.3"><path d="M6.6 10.8a15 15 0 0 0 6.6 6.6l2.2-2.2c.3-.3.7-.4 1-.2 1.1.4 2.3.6 3.6.6.6 0 1 .4 1 1V20c0 .6-.4 1-1 1A17 17 0 0 1 3 4c0-.6.4-1 1-1h3.5c.6 0 1 .4 1 1 0 1.3.2 2.5.6 3.6.1.3 0 .7-.2 1z"/></svg>
    <div><h5>Phone</h5><p>000-484-2790</p></div>
  </div>
  <div class="info-item" style="top:350px">
    <svg width="40" height="32" viewBox="0 0 40 32" fill="none" stroke="var(--green-light)" stroke-width="2"><rect x="2" y="4" width="36" height="24"/><path d="M2 4l18 14L38 4"/></svg>
    <div><h5>Email</h5><p>info@quillbylogistics.com</p></div>
  </div>
  <div class="field" style="left:540px;top:145px;width:230px">First Name</div>
  <div class="field" style="left:824px;top:145px;width:230px">Last Name</div>
  <div class="field" style="left:540px;top:220px;width:230px">Email</div>
  <div class="field" style="left:824px;top:220px;width:230px">Phone</div>
  <div class="field" style="left:540px;top:325px;width:514px">Message</div>
  <div class="btn abs" style="left:538px;top:389px;width:153px;height:52px;background:var(--green-light);font-size:17px">Submit</div>
</section>

<footer class="site-footer">
  <div class="brand abs" style="left:425px;top:40px">
    <div class="brand-dot" style="width:90px;height:90px"></div>
    <div class="brand-name" style="font-size:38px;color:var(--green-light)">Quillby Logistics</div>
  </div>
  <nav class="footer-nav"><span>Home</span><span>About</span><span>Services</span><span>Careers</span><span>Contact</span></nav>
  <div class="social"><i></i><i></i><i></i></div>
  <div class="copyright">© Copyright 2020 Quillby Logistics all rights reserved. <em>Legal Notice &nbsp;|&nbsp; Privacy Policy</em></div>
</footer>

</body>
</html>
```